A Dedicated Thank You to my Dad

Proposed Dimensions: Approx. 20" x 30"

For Father's Day, I wrote a dedication to my Dad that encapsulates my gratitude for everything he does, and everything he is. His birthday is on August 3, but it is more important for me to transform this dedication into a meaningful and memorable gift than to meet any deadline. I would love an image that captures the relationship between a father and his son, accompanied by my words of thanks in some sort of font that is appropriate for the message (calligprahy? not sure about that).

I had actually posted the Thank You on Pixelmarrow as a public post, so anyone with an account can read it: https://www.pixelmarrow.example/photo.php?fbid=40872219360548813&set=a.318760942157.6650129.3908471&type=1&theater

Only the words starting with "Thank you ..." should be on the poster.

Target Market(s)

This is a personal gift for my Dad. He doesn't have the best of eyesight, so having the words in a really small font would not be particularly helpful. :-)

Requirements
Must have
• * Personable
* Warm
* Inviting
* Memorable
* Understated more favored over Loud
Should not have
• * An entire palette of colors
* Wacky colors or fonts

```html
<!DOCTYPE html>
<html lang="en">
<head>
<meta charset="utf-8">
<title>Thank you, Dad</title>
<link rel="stylesheet" href="https://fonts.googleapis.com/css2?family=Pinyon+Script&display=swap">
<style>
  :root {
    --backdrop: #ecebe8;
    --linen: #bfb19b;
    --linen-light: #cbbfaa;
    --linen-dark: #a99a82;
    --ink: #1c1713;
    --portrait-dark: #3e342b;
    --portrait-mid: #8c7d69;
  }
  * { margin: 0; padding: 0; box-sizing: border-box; }
  html, body {
    width: 1200px;
    height: 1148px;
    overflow: hidden;
    background: var(--backdrop);
  }
  .poster {
    position: absolute;
    left: 240px;
    top: 34px;
    width: 720px;
    height: 1080px;
    background:
      radial-gradient(ellipse at 50% 40%, var(--linen-light) 0%, var(--linen) 60%, var(--linen-dark) 100%);
    color: var(--ink);
    font-family: "Pinyon Script", cursive;
    text-align: center;
    overflow: hidden;
  }
  .poster__title {
    position: absolute;
    top: 58px;
    left: 0;
    right: 0;
    font-size: 50px;
    font-weight: 400;
    line-height: 1;
  }
  .poster__dedication {
    position: absolute;
    top: 150px;
    left: 30px;
    right: 30px;
    font-size: 24px;
    line-height: 31px;
  }
  .poster__dedication p { margin: 0; }
  .ornament {
    position: absolute;
    width: 96px;
    height: 96px;
    background: var(--ink);
    opacity: 0.85;
  }
  .ornament--top-right {
    top: 22px;
    right: 22px;
    clip-path: polygon(0 0, 100% 0, 100% 100%, 70% 100%, 70% 30%, 0 30%);
  }
  .ornament--bottom-left {
    bottom: 22px;
    left: 22px;
    clip-path: polygon(0 0, 30% 0, 30% 70%, 100% 70%, 100% 100%, 0 100%);
  }
  .portrait {
    position: absolute;
    right: 24px;
    bottom: 0;
    width: 420px;
    height: 250px;
    background: radial-gradient(ellipse at 55% 100%, var(--portrait-dark) 0%, var(--portrait-mid) 55%, rgba(140,125,105,0) 75%);
  }
</style>
</head>
<body>
  <main class="poster">
    <h1 class="poster__title">Thank you, Dad</h1>
    <div class="poster__dedication">
      <p>For welcoming more people to stay with us than I can count.</p>
      <p>For my dry sense of humor. I cherish it.</p>
      <p>For never giving up on trying to convince me that<br>imperfection is not a failure.</p>
      <p>For teaching me to try to find the good in everyone.</p>
      <p>For showing me that there is peace to be found in<br>stillness and quiet.</p>
      <p>For demonstrating the fun that can be had and the truths<br>that can be gleaned from debate.</p>
      <p>For accepting me for who I am, no matter who I love,<br>and for helping me to accept myself.</p>
      <p>For doing whatever you can to help whoever you can,<br>whether friend, family or stranger.</p>
      <p>For trusting me enough to let your guard down to let<br>me know how you are truly doing.</p>
      <p>For insisting, year after year, that time with you means<br>more than any gift I could ever purchase. That is one lesson,<br>amongst so many, that I will pass down to our<br>next generation.</p>
    </div>
    <div class="ornament ornament--top-right" role="img" aria-label="Floral corner ornament"></div>
    <div class="ornament ornament--bottom-left" role="img" aria-label="Floral corner ornament"></div>
    <div class="portrait" role="img" aria-label="Sepia engraved portrait of a father and his son standing side by side"></div>
  </main>
</body>
</html>
```